Computer Company needs a Business card design

We need a business card design for our business. We assist people to transition to the QLX (Quorra Linkwave Exchange). The Australian Government-owned qlx™ network is a brand new telecommunications network currently being rolled out across Australia, giving access to a reliable broadband connection. Our niche market will predominantly be domestic customers in the 50+ age bracket. The assistance that we provide is everything from arranging the equipment, arranging the plan and contract term, appointment times, final testing of the network and any tweaks that need to be made. We basically PM the transition from start to finish. The business card design should be minimalist, should communicate loyalty and stability, should be easy to read and clearly explain what we do. We have asked for front and back. However, the back of the card does not have to include much information at all. It could be just a small design, or a repeat of our phone number. Up to you. The attached file only says what is required on the card. It does not specify where to arrange the text, what fonts to use, etc etc. As much as we would like to give you more info, due to our very limited design ability, we are not really able to send you any rough, or otherwise, designs of what we are after. Hopefully the above description is enough for you.

```html
<!DOCTYPE html>
<html lang="en">
<head>
<meta charset="utf-8">
<title>qlx Made Easy – Business Card</title>
<link href="https://fonts.googleapis.com/css2?family=Open+Sans:ital,wght@0,400;0,600;0,700;1,600&display=swap" rel="stylesheet">
<style>
  :root {
    --backdrop: #a9a9ae;
    --card: #ffffff;
    --ink-dark: #2b2b2d;
    --ink-mid: #6f6f73;
    --ink-soft: #8d8d92;
    --accent: #1a7fd4;
  }
  * { margin: 0; padding: 0; box-sizing: border-box; }
  html, body {
    width: 1200px; height: 863px; overflow: hidden;
    background: var(--backdrop);
    font-family: "Open Sans", Arial, sans-serif;
  }
  .stage {
    position: relative; width: 1200px; height: 863px;
    display: flex; flex-direction: column; align-items: center; justify-content: center; gap: 48px;
  }
  .card {
    width: 610px; height: 350px;
    background: var(--card);
    border-radius: 28px;
    box-shadow: 0 10px 24px rgba(0,0,0,0.22);
    position: relative;
    display: flex; flex-direction: column; align-items: center;
  }
  .card--front { justify-content: center; }
  .wordmark {
    display: flex; align-items: center; gap: 12px;
    font-weight: 700; color: var(--ink-dark);
    font-size: 54px; letter-spacing: -1px; line-height: 1;
  }
  .wordmark__dot {
    width: 14px; height: 14px; border-radius: 50%; background: var(--accent);
  }
  .card--back { padding-top: 70px; }
  .card--back .wordmark { font-size: 48px; }
  .tagline {
    margin-top: 14px;
    font-style: italic; font-weight: 600;
    font-size: 19px; color: var(--ink-dark);
  }
  .contact {
    margin-top: 34px;
    display: flex; flex-direction: column; align-items: center; gap: 8px;
    color: var(--ink-mid);
  }
  .contact__name { font-weight: 700; font-size: 20px; color: var(--ink-mid); }
  .contact__line {
    display: flex; align-items: center; gap: 8px;
    font-size: 15px; color: var(--ink-soft);
  }
  .contact__line svg { width: 14px; height: 14px; fill: none; stroke: var(--ink-soft); stroke-width: 1.6; }
</style>
</head>
<body>
<main class="stage">
  <section class="card card--front" aria-label="Card front">
    <div class="wordmark"><span class="wordmark__dot"></span>qlx Made Easy</div>
  </section>

  <section class="card card--back" aria-label="Card back">
    <div class="wordmark"><span class="wordmark__dot"></span>qlx Made Easy</div>
    <p class="tagline">‘We organise your qlx from start to finish’</p>
    <div class="contact">
      <p class="contact__name">Reid Callaway</p>
      <p class="contact__line">
        <svg viewBox="0 0 16 16" aria-hidden="true"><path d="M4 1.5l2.5 3-1.5 1.5c.8 2 2.5 3.7 4.5 4.5l1.5-1.5 3 2.5-1.5 2.5C7.5 14 2 8.5 1.5 3z"/></svg>
        0491 570 238
      </p>
      <p class="contact__line">
        <svg viewBox="0 0 16 16" aria-hidden="true"><rect x="1.5" y="3.5" width="13" height="9" rx="1"/><path d="M1.5 4l6.5 5 6.5-5"/></svg>
        reid@qlxmadeeasy.com.au
      </p>
    </div>
  </section>
</main>
</body>
</html>
```